Website design for dressage horse training business

Looking to develop a new website design for a dressage horse training website. We want to change from a single landing page to one with multiple pages.
You are free to use your creativity to design the main landing page. This is the only page you need to design at this point. I would encourage looking at other Dressage Training websites to get a feel for what is typically on them. A few websites are listed below although I think the design of them could be better.
Notes:
- Menu to include: Home, Services, News Room, Blog, About Us, Contact,
- FAQ section on main page
- Logo to remain the same - the logo attached is not the correct color so change to match existing color.
- Change 'Sponsors' to 'Partnerships' on main page
Here is the link to the current site:
https://lindenridgestables.com/
Example sites
https://www.crestwoodsporthorsesco.com/
https://corinnalavelledressage.com/
Target Market(s)
Older women with disposable income
Number of Pages Required
1 page
Look and feel
Each slider illustrates characteristics of the customer's brand and the style your logo design should communicate.

```html
<!DOCTYPE html>
<html lang="en">
<head>
<meta charset="utf-8">
<title>Linden Ridge Stables — Dressage &amp; Sport Horse Training</title>
<link href="https://fonts.googleapis.com/css2?family=Mulish:ital,wght@0,400;0,600;0,700;0,800;1,700;1,800&display=swap" rel="stylesheet">
<style>
:root{
  --black:#000;
  --ink:#1c1c1c;
  --text:#333;
  --white:#fff;
  --tan:#c39f7b;
  --tan-dark:#8a6a4c;
  --maroon:#5a0a0a;
  --panel:#1b1b1b;
  --band:#2b2b2b;
  --faq:#141414;
  --placeholder:#3a3a3a;
}
*{box-sizing:border-box;margin:0;padding:0}
html,body{width:1200px;height:3884px;overflow:hidden;background:var(--black)}
body{position:relative;font-family:'Mulish',sans-serif;color:var(--white)}
.abs{position:absolute}
.header{left:0;top:0;width:1200px;height:77px;background:var(--black);z-index:3}
.brand{left:134px;top:12px;color:var(--tan);font-weight:400;line-height:1.1}
.brand .name{font-size:30px;letter-spacing:1px}
.brand .sub{font-size:11px;letter-spacing:9px;margin-top:4px}
.nav{top:44px;left:523px;display:flex;gap:34px;font-size:14px;font-weight:600}
.nav a{color:var(--white);text-decoration:none}
.nav a.active{color:var(--tan)}
.nav-dot{left:532px;top:20px;width:12px;height:16px;border-radius:50% 50% 40% 40%;background:var(--tan-dark)}
.btn{display:flex;align-items:center;justify-content:center;font-size:15px;text-decoration:none}
.btn-tan{background:var(--tan);color:var(--white)}
.header .btn-tan{left:894px;top:27px;width:155px;height:37px}
.hero{left:0;top:77px;width:1200px;height:500px;background:linear-gradient(180deg,#5e6b45 0%,#6b5c48 40%,#3a3328 72%,#000 100%)}
.hero-title{left:0;top:475px;width:1200px;text-align:center;font-style:italic;font-weight:800;font-size:40px;line-height:47px}
.photo{background:linear-gradient(135deg,#6f7a4a,#3f3a2c)}
.card{background:var(--white);color:var(--text)}
.card h2{font-size:33px;font-weight:800;font-style:italic;color:var(--ink);margin-bottom:14px}
.card p{font-size:12px;line-height:23px;margin-bottom:8px}
.training-photo{left:134px;top:643px;width:537px;height:394px}
.training-card{left:515px;top:756px;width:536px;height:366px;padding:30px 24px 30px 30px}
.training-card .btn{width:156px;height:37px;margin-top:10px}
.lessons-ghost{left:330px;top:1180px;font-size:120px;font-weight:800;color:#1a1a1a;letter-spacing:4px;line-height:1}
.lessons-title{left:211px;top:1232px;font-size:31px;font-weight:800;font-style:italic}
.lessons-rule{left:463px;top:1210px;width:2px;height:56px;background:var(--tan-dark)}
.lessons-text{left:496px;top:1200px;width:490px;font-size:12.5px;line-height:23px;font-weight:600}
.lessons-text em{display:block;margin-top:8px;font-size:13.5px;font-weight:700}
.partner-photo{left:134px;top:1369px;width:255px;height:377px;background:linear-gradient(160deg,#a89a80,#6d6a5a 60%,#3b3a33)}
.partner-title{left:436px;top:1363px;font-size:32px;font-weight:800;font-style:italic}
.partner-rule{left:445px;top:1450px;width:2px;height:147px;background:var(--tan-dark)}
.partner-slot{background:var(--placeholder)}
.slot-wide{left:466px;top:1437px;width:148px;height:50px}
.slot-square{left:512px;top:1512px;width:56px;height:56px}
.partner-name{left:676px;top:1470px;width:360px;text-align:center;color:var(--tan-dark);font-size:44px;font-weight:700;line-height:1.1}
.partner-card{left:440px;top:1643px;width:613px;height:200px;padding:22px 18px}
.partner-card p{font-size:12.5px;line-height:24px;margin-bottom:4px}
.partner-card strong{color:var(--maroon);font-weight:600}
.btn-maroon{background:var(--maroon);color:var(--white);width:128px;height:37px;margin-top:8px}
.mission{left:165px;top:1920px;width:854px;height:110px;background:var(--panel);box-shadow:0 0 14px rgba(255,255,255,.12);display:flex;align-items:center;justify-content:center;text-align:center;padding:0 22px;font-size:13.5px;line-height:25px}
.sale-photo{left:515px;top:2101px;width:536px;height:395px;background:linear-gradient(110deg,#8aa06a 0%,#d9ddd0 35%,#4a2c1e 60%,#2c1a12 100%)}
.sale-vertical{left:1000px;top:2120px;writing-mode:vertical-rl;font-size:38px;color:rgba(120,120,120,.85);font-weight:600}
.sale-card{left:134px;top:2213px;width:536px;height:367px;padding:38px 27px}
.sale-card p{font-size:12px}
.faq-title{left:0;top:2650px;width:1200px;text-align:center;font-size:32px;font-weight:800;font-style:italic}
.faq-photo{left:134px;top:2719px;width:456px;height:378px;background:linear-gradient(180deg,#d6c6a8,#c5b08c)}
.faq-list{left:607px;top:2719px;width:395px}
.faq-item{background:var(--faq);box-shadow:0 0 8px rgba(255,255,255,.08);margin-bottom:8px;padding:12px 20px;position:relative;font-size:12px;color:var(--tan)}
.faq-item .chev{position:absolute;right:18px;top:16px;width:8px;height:8px;border-right:1.5px solid var(--tan);border-bottom:1.5px solid var(--tan);transform:rotate(45deg)}
.faq-item.open .chev{transform:rotate(-135deg);top:20px}
.faq-item p{color:#ddd;font-size:10.5px;line-height:19px;margin-top:5px}
.contact-band{left:0;top:3178px;width:1200px;height:316px;background:var(--band);text-align:center}
.contact-band h2{margin-top:82px;color:var(--tan);font-size:33px;font-weight:800;font-style:italic}
.contact-band .lead{margin:10px auto 0;width:800px;font-size:18px;line-height:30px;font-style:italic;font-weight:700}
.contact-row{position:absolute;left:0;width:1200px;top:210px;display:flex;justify-content:center;align-items:center;gap:12px}
.contact-row .btn{height:37px;padding:0 14px}
.contact-row .or{font-size:24px}
.btn-dark{background:var(--black);color:var(--white);gap:8px}
.footer-head{font-size:17px;color:var(--tan);font-weight:600}
.about{left:134px;top:3573px;width:340px}
.about p{margin-top:12px;font-size:12.5px;line-height:23px}
.about a{color:var(--tan);text-decoration:none}
.details{left:551px;top:3573px;width:260px}
.detail{display:flex;gap:16px;margin-top:18px;font-size:12.5px;line-height:21px}
.detail svg{flex:none}
.foot-brand{left:826px;top:3605px;width:224px;text-align:center;color:var(--tan);font-size:30px;font-weight:400;line-height:1.1}
.foot-brand .sub{font-size:12px;letter-spacing:8px;margin-top:6px}
.socials{left:868px;top:3681px;display:flex;gap:6px}
.socials span{width:30px;height:30px;border:1px solid #555}
.foot-rule{left:134px;top:3834px;width:916px;height:1px;background:#333}
.copyright{left:0;top:3848px;width:1200px;text-align:center;font-size:12.5px}
</style>
</head>
<body>
<header class="abs header">
  <div class="abs brand"><div class="name">LINDEN RIDGE</div><div class="sub">STABLES</div></div>
  <span class="abs nav-dot"></span>
  <nav class="abs nav">
    <a class="active" href="#">Home</a><a href="#">Services</a><a href="#">News</a><a href="#">Blog</a><a href="#">About Us</a>
  </nav>
  <a class="abs btn btn-tan" href="#">Contact Us Today</a>
</header>

<div class="abs hero" role="img" aria-label="Rider on a pinto horse in front of a wooden barn"></div>
<h1 class="abs hero-title">Central Iowa’s Premier<br>Dressage And Sport Horse Training</h1>

<div class="abs photo training-photo" role="img" aria-label="Rider schooling a bay horse outdoors"></div>
<section class="abs card training-card">
  <h2>Horse Training</h2>
  <p>Linden Ridge Stables offers both full and half time training options with Clara Whitfield. There is much flexibility with both rides and/or lessons weekly in the training packages that can be customized to fit both the horse and the rider’s needs.</p>
  <p>Generally, full training provides 3-4 “working days” of riding, and 1-2 “light” days consisting of cavelletti/jumping, hacking or lunging depending on the horse’s personality, their needs, and the training goals.</p>
  <p>Clara’s empathetic and cross-training techniques create horses who are happy and content in their jobs, while building strength and endurance for the dressage ring.</p>
  <a class="btn btn-tan" href="#">Know More</a>
</section>

<div class="abs lessons-ghost">LESSONS</div>
<h2 class="abs lessons-title">Horse Lessions</h2>
<span class="abs lessons-rule"></span>
<div class="abs lessons-text">Lessons are available for all ages of riders. Clara thoroughly enjoys working with accomplished riders looking to succeed in the show ring, as well as riders just wanting to learn what dressage is about.<em>Come join our incredible and encouraging team!</em></div>

<div class="abs partner-photo" role="img" aria-label="Trainer standing in an arena"></div>
<h2 class="abs partner-title">Our Partnerships With</h2>
<span class="abs partner-rule"></span>
<span class="abs partner-slot slot-wide" role="img" aria-label="Partner badge"></span>
<span class="abs partner-slot slot-square" role="img" aria-label="Partner badge"></span>
<div class="abs partner-name">LINDEN RIDGE<br>STABLES</div>
<section class="abs card partner-card">
  <p><strong>Fieldcraft Saddlery</strong> is constantly designing and researching saddles and riders to find the right blend of design and craftsmanship to fit today’s demands. Every saddle’s detail is carefully checked to be sure the workmanship and quality is there.</p>
  <p>&nbsp;All saddles are anatomically designed for horse and rider, hand-crafted from the finest leathers, and manufactured using the most technically advanced methods and features available.</p>
  <a class="btn btn-maroon" href="#">Visit Webiste</a>
</section>

<div class="abs mission">Our misssion lorem ipsum dolor sit amet, consectetuer adipiscing elit, sed diam nonummy nibh euismod tincidunt ut laoreet dolore magna aliquam erat volt wisi enim ad minim veniam, quis nostrud exerci tation ullamcorper suscipit lobortis.</div>

<div class="abs sale-photo" role="img" aria-label="Head of a dark bay horse with braided mane against white flowers"></div>
<div class="abs sale-vertical">Silver Meridian</div>
<section class="abs card sale-card">
  <h2>Horse For Sale</h2>
  <p>Silver Meridian, “Milo,” (Cortez x Harbor Pilot) is a 2012, 16hh imported Hanoverian. Milo is an incredibly quiet and kind horse. He is ridden by both an amatuer and child rider. He loves to hack and is very quiet alone and with a group of horses.&nbsp; He has shown through first level with scores into the 70’s at both training and first level. Milo is currently solidly schooling all of second level, as well as half passes and flying changes from third level.</p>
  <p>Milo has 3 very easy to ride gaits and it is easy for riders to sit his trot. Very quiet and well mannered on the ground with vet, farrier and clipping. He has lovely confirmation with a striking head. He is regularly admired at shows! Milo is very versatile and game and also loves to jump!</p>
</section>

<h2 class="abs faq-title">Frequently Asked Questions</h2>
<div class="abs faq-photo" role="img" aria-label="Legs of a chestnut horse and rider's boots in a sand arena"></div>
<div class="abs faq-list">
  <div class="faq-item open">Diam nonummy nibh euismod tincidunt ut laoreet&nbsp; ?<span class="chev"></span><p>Lorem ipsum dolor sit amet, consectetuer adipiscing elit, sed diam nonummy nibh euismod tincidunt ut laoreet dolore magn.</p></div>
  <div class="faq-item">What paperwork do I need to donate my Horse<span class="chev"></span></div>
  <div class="faq-item">Laoreet dolore magna aliquam erat fdsf ?<span class="chev"></span></div>
  <div class="faq-item">Dolor sit amet consectetuer adipiscing elit ?<span class="chev"></span></div>
  <div class="faq-item">Lorem ipsum dolor sit amet consectetuer adipiscing elit ?<span class="chev"></span></div>
  <div class="faq-item">Dolor sit amet consectetuer adipiscing elit ?<span class="chev"></span></div>
  <div class="faq-item">Lorem ipsum dolor sit amet consectetuer adipiscing elit ?<span class="chev"></span></div>
</div>

<section class="abs contact-band">
  <h2>Contact Me</h2>
  <p class="lead">If you are interested in learning more about Linden Ridge Stables’ services or availability for training or lessons, please contact us below!</p>
  <div class="contact-row">
    <a class="btn btn-tan" href="#" style="color:var(--ink)">Contact Us Today</a>
    <span class="or">Or</span>
    <a class="btn btn-dark" href="#"><svg width="18" height="18" viewBox="0 0 24 24" fill="none" stroke="#c39f7b" stroke-width="1.8"><path d="M5 3h4l2 5-2.5 1.5a11 11 0 0 0 6 6L16 13l5 2v4a2 2 0 0 1-2 2A16 16 0 0 1 3 5a2 2 0 0 1 2-2z"/></svg>515-555-0182</a>
  </div>
</section>

<section class="abs about">
  <h3 class="footer-head">About Linden Ridge</h3>
  <p>FEI rider and trainer, Clara Whitfield began her riding career at a young age. She went up through the ranks of Pony Club and with an emphasis &amp; focus in eventing. During college, Clara worked for a small breeder starting young horses. Clara loves starting young horses including starting and guiding them in a correct and quiet way to help them flourish....<a href="#">Read More</a></p>
</section>

<section class="abs details">
  <h3 class="footer-head">Contact Details</h3>
  <div class="detail"><svg width="32" height="32" viewBox="0 0 32 32" fill="none" stroke="#c39f7b"><circle cx="16" cy="16" r="15"/><path d="M16 24s-5-5.5-5-9a5 5 0 0 1 10 0c0 3.5-5 9-5 9z"/><circle cx="16" cy="15" r="1.6"/></svg><span>Linden Ridge Stables<br>Ankeny, IA 50021</span></div>
  <div class="detail"><svg width="32" height="32" viewBox="0 0 32 32" fill="none" stroke="#c39f7b"><circle cx="16" cy="16" r="15"/><path d="M11 9h3l1.5 3.5-1.8 1a7 7 0 0 0 3.8 3.8l1-1.8L22 17v3a1.5 1.5 0 0 1-1.5 1.5A11 11 0 0 1 9.5 10.5 1.5 1.5 0 0 1 11 9z"/></svg><span>Phone<br>515.555.0182</span></div>
  <div class="detail"><svg width="32" height="32" viewBox="0 0 32 32" fill="none" stroke="#c39f7b"><circle cx="16" cy="16" r="15"/><rect x="9" y="11" width="14" height="10"/><path d="M9 11l7 6 7-6"/></svg><span>Email<br>inquiry@lindenridgestables.com</span></div>
</section>

<div class="abs foot-brand">LINDEN RIDGE<div class="sub">STABLES</div></div>
<div class="abs socials" aria-label="Social links"><span></span><span></span><span></span><span></span></div>

<span class="abs foot-rule"></span>
<p class="abs copyright">Copyright © 2021 Linden Ridge Stables. All Rights Reserved.</p>
</body>
</html>
```